Counseling business card, clean but alluring

I need it to appeal to all ages and men. I’m planning to use my current logo. I like crisp and clean. Possibly some shimmer. My website is harborleafwellness.net

Contact Information for Business Card

Marissa "Missy" Dolan Pryce, LPC, RPT

harborleafwellness.net

28159 Larkspur Avenue, Suite 407
Addison TX 75094

469-315-2984 | missy@harborleafwellness.net

Colors
0355a3
85cae6
fbee3e
ffffff
33b8a4
0692cd

Requirements
Must have
• My logo

```html
<!DOCTYPE html>
<html lang="en">
<head>
<meta charset="UTF-8">
<title>Harborleaf Wellness — Business Card</title>
<link rel="stylesheet" href="https://fonts.googleapis.com/css2?family=Marcellus&family=Questrial&display=swap">
<style>
  :root {
    --backdrop: #1d1d1f;
    --card: #ffffff;
    --ink: #5a5a5c;
    --ink-soft: #4a4a4c;
    --gold: #c8952f;
    --gold-light: #e3bd73;
  }
  * { box-sizing: border-box; margin: 0; padding: 0; }
  html, body {
    width: 1200px;
    height: 1189px;
    overflow: hidden;
    background: var(--backdrop);
  }
  .canvas {
    width: 1200px;
    height: 1189px;
    display: flex;
    flex-direction: column;
    align-items: center;
    justify-content: center;
    gap: 60px;
  }
  .card {
    width: 900px;
    height: 514px;
    background: var(--card);
    border-radius: 40px;
    position: relative;
    overflow: hidden;
  }

  /* Front */
  .card--front {
    display: flex;
    align-items: center;
    justify-content: center;
    gap: 28px;
  }
  .brand-mark {
    width: 64px;
    height: 64px;
    border-radius: 50%;
    background: var(--gold);
    flex: none;
  }
  .brand-name {
    font-family: "Marcellus", serif;
    font-weight: 400;
    color: var(--ink);
    letter-spacing: 1px;
  }
  .card--front .brand-name { font-size: 64px; }

  /* Back */
  .card--back { padding: 70px 0 0 80px; }
  .card--back .brand-name { font-size: 46px; margin-bottom: 26px; }
  .person {
    font-family: "Questrial", sans-serif;
    color: var(--ink-soft);
    font-size: 28px;
    letter-spacing: 0.5px;
  }
  .role {
    font-family: "Questrial", sans-serif;
    color: var(--gold);
    font-size: 20px;
    letter-spacing: 1px;
    text-transform: uppercase;
    margin-top: 4px;
  }
  .address {
    font-family: "Questrial", sans-serif;
    color: var(--ink-soft);
    font-size: 22px;
    line-height: 1.3;
    font-style: normal;
    margin-top: 34px;
  }
  .contact-list {
    list-style: none;
    margin-top: 22px;
    font-family: "Questrial", sans-serif;
    color: var(--ink-soft);
    font-size: 22px;
    line-height: 1.35;
  }
  .contact-list li {
    display: flex;
    align-items: center;
    gap: 18px;
  }
  .contact-icon {
    width: 18px;
    height: 18px;
    flex: none;
    fill: var(--gold);
  }
  .back-mark {
    position: absolute;
    right: 90px;
    top: 110px;
    width: 250px;
    height: 250px;
    border-radius: 50%;
    background: radial-gradient(circle at 40% 35%, var(--gold-light), var(--gold));
  }
</style>
</head>
<body>
<main class="canvas">
  <section class="card card--front" aria-label="Card front">
    <span class="brand-mark" aria-hidden="true"></span>
    <span class="brand-name">Harborleaf Wellness</span>
  </section>

  <section class="card card--back" aria-label="Card back">
    <div class="brand-name">Harborleaf Wellness</div>
    <div class="person">Marissa Dolan Pryce, LPC, RPT</div>
    <div class="role">Counselor and Play Therapist</div>
    <address class="address">
      28159 Larkspur Avenue<br>
      Suite 407 Addison, TX 75094
    </address>
    <ul class="contact-list">
      <li>
        <svg class="contact-icon" viewBox="0 0 24 24" aria-hidden="true"><path d="M6.6 10.8a15.1 15.1 0 0 0 6.6 6.6l2.2-2.2a1 1 0 0 1 1-.25 11.4 11.4 0 0 0 3.6.57 1 1 0 0 1 1 1V20a1 1 0 0 1-1 1A17 17 0 0 1 3 4a1 1 0 0 1 1-1h3.5a1 1 0 0 1 1 1c0 1.25.2 2.45.57 3.57a1 1 0 0 1-.25 1z"/></svg>
        469-315-2984
      </li>
      <li>
        <svg class="contact-icon" viewBox="0 0 24 24" aria-hidden="true"><path d="M2 5h20v14H2z M2 5l10 8 10-8" fill="var(--gold)" stroke="#fff" stroke-width="1.2"/></svg>
        missy@harborleafwellness.net
      </li>
      <li>
        <svg class="contact-icon" viewBox="0 0 24 24" aria-hidden="true"><g fill="none" stroke="var(--gold)" stroke-width="1.8"><circle cx="12" cy="12" r="9.5"/><ellipse cx="12" cy="12" rx="4" ry="9.5"/><path d="M2.5 12h19M4 7h16M4 17h16"/></g></svg>
        www.harborleafwellness.net
      </li>
    </ul>
    <span class="back-mark" aria-hidden="true"></span>
  </section>
</main>
</body>
</html>
```